Wedding design for Olav & Marte (Monogram, Banner, designelements, etc.)

We are looking for a design that goes through the entire wedding from the invitations to decor at the actual wedding party. Specific things we want is a monogram of our initials "O" from "Olav"(Groom) and "M" from "Marte"(Bride). We also want a banner that can be used for, for example webpage / facebook, and several design elements that can be used for invitations, songs, etc. . We also want our wedding date to come trough, as this is a little special. "18.08.18" is the date and the number "8" is identical to the eternity symbol, something we want to focus on in the design.

Have added some pictures of us, but it's up to the designer and choose if they will be used. And if used, it's great if the design is not locked to some images, but that the images can be replaced afterwards.

Reason: We have now changed the payment guaranteed and specified our wishes

Reason: Many of you have made great monograms (Corvadel, Quonbix7ta, Dorumi, WTatelier and nordic hue) But in the brief we have asked for a banner and some designelements we can use in different types of prints. Such as invitations, songs, menus etc.

Industry/Entity Type

Wedding

Font styles to use
Serif
Script

Colors

Designer to choose colors to be used in the design.

Requirements
Must have
• Monogram, Banner for facebook/webpage, Design elements for use on invitations, songs, signs, and other printed material.
Nice to have
• -Unique/special presentation of our wedding date and names. And nice implementation of the eternity symbol.
• -That the various design components can be used separately as well as together
Should not have
• Not too much details.

```html
<!DOCTYPE html>
<html lang="en">
<head>
<meta charset="utf-8">
<title>Olav &amp; Marte – Wedding Card</title>
<link href="https://fonts.googleapis.com/css2?family=Pinyon+Script&display=swap" rel="stylesheet">
<style>
  :root {
    --paper: #ffffff;
    --frame: #222222;
    --ink: #2a2a2a;
    --lavender: #d4cce4;
    --navy: #4b5389;
    --blush: #ee9f99;
    --peach: #fbd5bf;
    --cream: #fdf2ea;
  }
  html, body {
    margin: 0;
    padding: 0;
    width: 1200px;
    height: 1200px;
    overflow: hidden;
    background: var(--paper);
  }
  .canvas {
    position: relative;
    width: 1200px;
    height: 1200px;
    background: var(--paper);
  }
  .card {
    position: absolute;
    left: 229px;
    top: 58px;
    width: 765px;
    height: 1082px;
    border: 1px solid var(--frame);
    box-sizing: border-box;
    overflow: hidden;
    background: var(--paper);
  }
  .monogram {
    position: absolute;
    left: 0;
    top: 70px;
    width: 100%;
    text-align: center;
    font-family: "Pinyon Script", cursive;
    font-size: 210px;
    line-height: 1;
    color: var(--lavender);
    letter-spacing: -60px;
    margin: 0;
    font-weight: 400;
  }
  .message {
    position: absolute;
    left: 0;
    top: 330px;
    width: 100%;
    margin: 0;
    text-align: center;
    font-family: "Pinyon Script", cursive;
    font-size: 23px;
    line-height: 35.5px;
    color: var(--ink);
  }
  .divider {
    position: absolute;
    left: 135px;
    top: 654px;
    width: 496px;
    height: 108px;
    border-radius: 54px;
    background: radial-gradient(ellipse at center, rgba(75,83,137,0.22), rgba(75,83,137,0.06) 70%, rgba(75,83,137,0) 100%);
  }
  .floral-border {
    position: absolute;
    left: 0;
    bottom: 0;
    width: 765px;
    height: 243px;
    display: block;
  }
</style>
</head>
<body>
<div class="canvas">
  <div class="card">
    <h1 class="monogram">OM</h1>

    <p class="message">
      Some small text Some small text Some small text<br>
      Some small text Some small text Some small text Some small text Some<br>
      small text Some small text Some small text<br>
      Some small text Some small text Some small text Some small text Some<br>
      small text Some small text Some small text
    </p>

    <div class="divider" role="img" aria-label="Navy calligraphic flourish divider"></div>

    <svg class="floral-border" viewBox="0 0 765 243" role="img" aria-label="Pastel floral pattern of pink leaves, peach blossoms and lavender flowers beneath a wavy lavender ribbon">
      <defs>
        <linearGradient id="floral-tones" x1="0" y1="0" x2="1" y2="1">
          <stop offset="0" stop-color="#f6c9c0"/>
          <stop offset="0.3" stop-color="#f3b4ab"/>
          <stop offset="0.55" stop-color="#e9d4e2"/>
          <stop offset="0.8" stop-color="#f7c7b6"/>
          <stop offset="1" stop-color="#f1b0a8"/>
        </linearGradient>
      </defs>
      <path class="floral-fill"
        d="M -1 12 C 19 12 33 44 53 44 S 87 12 107 12 S 141 44 161 44 S 195 12 215 12 S 249 44 269 44 S 303 12 323 12 S 357 44 377 44 S 411 12 431 12 S 465 44 485 44 S 519 12 539 12 S 573 44 593 44 S 627 12 647 12 S 681 44 701 44 S 735 12 755 12 S 789 44 809 44 L 809 243 L -1 243 Z"
        fill="url(#floral-tones)"/>
      <path class="ribbon"
        d="M -55 44 C -35 44 -21 12 -1 12 S 33 44 53 44 S 87 12 107 12 S 141 44 161 44 S 195 12 215 12 S 249 44 269 44 S 303 12 323 12 S 357 44 377 44 S 411 12 431 12 S 465 44 485 44 S 519 12 539 12 S 573 44 593 44 S 627 12 647 12 S 681 44 701 44 S 735 12 755 12 S 789 44 809 44"
        fill="none" stroke="var(--lavender)" stroke-width="22"/>
    </svg>
  </div>
</div>
</body>
</html>
```